Cole Varga Photography

Would like the Business card to have a cool logo. I’m targeting wedding/ engagement: portrait photography. My phone number on it. And my business email address.

Wedding/portrait/engagement photography.

```html
<!DOCTYPE html>
<html lang="en">
<head>
<meta charset="utf-8">
<title>Cole Varga Photography – Business Card</title>
<link href="https://fonts.googleapis.com/css2?family=Cinzel:wght@600&family=Montserrat:wght@400;500;600&display=swap" rel="stylesheet">
<style>
  :root {
    --backdrop: #3a3b3e;
    --card-black: #0c0b0b;
    --cell-dark: #1b1717;
    --cell-deep: #0a0909;
    --accent: #f2cc1f;
    --frame-gold: #8c7633;
    --text-light: #f1f1f1;
    --text-muted: #d6d6d6;
  }
  * { margin: 0; padding: 0; box-sizing: border-box; }
  html, body { width: 1200px; height: 862px; overflow: hidden; }
  body { background: var(--backdrop); position: relative; font-family: "Montserrat", sans-serif; }

  .card {
    position: absolute; left: 280px; width: 640px; height: 366px;
    background: var(--card-black); overflow: hidden;
    box-shadow: 0 10px 28px rgba(0,0,0,.45);
  }
  .card--front { top: 40px; }
  .card--back { top: 456px; }

  /* Front grid */
  .photo-grid {
    position: absolute; inset: 0;
    display: grid; grid-template-columns: repeat(5, 1fr); grid-template-rows: repeat(3, 1fr);
  }
  .cell { background: var(--cell-dark); }
  .cell--deep { background: var(--cell-deep); }
  .photo { background: linear-gradient(135deg, #6d6461, #c9bfb9 55%, #8a7f79); }
  .photo--rings { background: linear-gradient(140deg, #b6aba3, #ebe3dc 50%, #7d726b); }
  .photo--couple { background: linear-gradient(120deg, #2c2727, #8e8580 60%, #4a4342); }
  .photo--bouquet { background: linear-gradient(150deg, #4d4544, #c8bdb6 50%, #6f6563); }
  .photo--hands { background: linear-gradient(110deg, #3a3434, #d7d0cb 55%, #5c5453); }
  .photo--bride { background: linear-gradient(160deg, #3e3835, #9a918b 45%, #e0d9d3 75%); }

  .brand { position: absolute; display: flex; flex-direction: column; }
  .card--front .brand {
    left: 128px; top: 122px; width: 384px; height: 122px;
    background: var(--cell-deep);
    justify-content: center; padding-left: 18px;
  }
  .brand__row { display: flex; align-items: center; gap: 12px; }
  .brand__dot {
    width: 30px; height: 30px; border-radius: 50%; background: var(--accent); flex: none;
  }
  .brand__name {
    font-family: "Cinzel", serif; font-weight: 600; color: var(--accent);
    font-size: 20px; letter-spacing: .4px; line-height: 1.1; white-space: nowrap;
  }
  .brand__services {
    margin-top: 14px; padding-left: 42px; white-space: nowrap;
    color: var(--text-light); font-size: 10.5px; font-weight: 500; letter-spacing: 1.6px;
  }
  .brand__services span { margin: 0 7px; }

  /* Back */
  .backdrop-photo {
    position: absolute; inset: 0;
    background: radial-gradient(ellipse at 45% 55%, #2a2726 0%, #141212 45%, var(--card-black) 80%);
  }
  .frame { position: absolute; inset: 16px; border: 1.5px solid var(--frame-gold); }
  .card--back .brand { left: 110px; top: 78px; }
  .card--back .brand__dot { width: 34px; height: 34px; }
  .card--back .brand__name { font-size: 25px; }
  .card--back .brand__services { padding-left: 46px; }

  .divider {
    position: absolute; left: 40px; right: 40px; top: 200px;
    border-top: 2px dotted rgba(255,255,255,.55);
  }
  .contacts {
    position: absolute; left: 40px; right: 40px; top: 228px;
    display: grid; grid-template-columns: 1fr 1.3fr 1fr; column-gap: 20px;
  }
  .contact { display: flex; flex-direction: column; align-items: center; text-align: center; gap: 12px; }
  .contact__icon {
    width: 34px; height: 34px; background: var(--accent);
    display: flex; align-items: center; justify-content: center;
  }
  .contact__text { color: var(--text-muted); font-size: 11.5px; line-height: 1.5; letter-spacing: .2px; white-space: nowrap; }
</style>
</head>
<body>

<section class="card card--front" aria-label="Business card front">
  <div class="photo-grid">
    <div class="cell"></div>
    <div class="cell cell--deep"></div>
    <div class="cell"></div>
    <div class="cell photo" role="img" aria-label="Black and white portrait of a young bride with a flower crown"></div>
    <div class="cell photo photo--rings" role="img" aria-label="Wedding rings resting on flowers"></div>

    <div class="cell photo photo--couple" role="img" aria-label="Couple embracing in soft light"></div>
    <div class="cell cell--deep"></div>
    <div class="cell cell--deep"></div>
    <div class="cell cell--deep"></div>
    <div class="cell photo photo--bouquet" role="img" aria-label="Bride holding a rose bouquet"></div>

    <div class="cell photo photo--hands" role="img" aria-label="Bride and groom holding hands"></div>
    <div class="cell"></div>
    <div class="cell photo photo--bride" role="img" aria-label="Bride outdoors with bouquet"></div>
    <div class="cell cell--deep"></div>
    <div class="cell"></div>
  </div>

  <div class="brand">
    <div class="brand__row">
      <div class="brand__dot"></div>
      <div class="brand__name">COLE VARGA PHOTOGRAPHY</div>
    </div>
    <div class="brand__services">MARRIAGE<span>|</span>POTRAIT<span>|</span>ENGAGEMENT</div>
  </div>
</section>

<section class="card card--back" aria-label="Business card back">
  <div class="backdrop-photo" role="img" aria-label="Faint dark photo of hands holding a camera"></div>
  <div class="frame"></div>

  <div class="brand">
    <div class="brand__row">
      <div class="brand__dot"></div>
      <div class="brand__name">COLE VARGA PHOTOGRAPHY</div>
    </div>
    <div class="brand__services">MARRIAGE<span>|</span>POTRAIT<span>|</span>ENGAGEMENT</div>
  </div>

  <div class="divider"></div>

  <div class="contacts">
    <div class="contact">
      <div class="contact__icon">
        <svg width="20" height="20" viewBox="0 0 20 20" fill="none" stroke="#111" stroke-width="1.6" stroke-linecap="round">
          <path d="M3 8c0-2.5 3-4 7-4s7 1.5 7 4l-1 2-3-1V7H7v2l-3 1z"/>
          <path d="M5 15h10"/>
        </svg>
      </div>
      <div class="contact__text">+00 555 014 236<br>+00 555 014 237</div>
    </div>
    <div class="contact">
      <div class="contact__icon">
        <svg width="20" height="20" viewBox="0 0 20 20" fill="none" stroke="#111" stroke-width="1.6" stroke-linecap="round">
          <rect x="6" y="4" width="8" height="13" rx="4"/>
          <path d="M10 4v4"/>
        </svg>
      </div>
      <div class="contact__text">info@colevarga.com<br>www.colevargaphotography.com</div>
    </div>
    <div class="contact">
      <div class="contact__icon">
        <svg width="20" height="20" viewBox="0 0 20 20" fill="none" stroke="#111" stroke-width="1.6" stroke-linejoin="round">
          <rect x="3" y="5" width="14" height="10"/>
          <path d="M3 5l7 6 7-6"/>
        </svg>
      </div>
      <div class="contact__text">48, Linden Row, Harbor City,<br>Vermont 205417</div>
    </div>
  </div>
</section>

</body>
</html>
```